Brightfernrx website

We are a weight loss clinic and we need a website built. please look at these websites for content and style. Just need like 5 pages see samples. AI files of logo are not avail yet so use sample for place set

https://glowshiftstudio.com/
ortanvital.com
https://pinecrestclinicalbodybalance.com/
https://yourslimmingnook.com/
https://qrvskinstudio.com/treatments/weight-loss-injections/

Target Market(s)

Women

Industry/Entity Type

weight loss

Coding

Coded - Design and coding required

Number of Pages Required

5+ page

Requirements
Nice to have
• please make look like a medspa website

```html
<!DOCTYPE html>
<html lang="en">
<head>
<meta charset="utf-8">
<title>Brightfernrx — Wellness and Weight Loss</title>
<link rel="stylesheet" href="https://fonts.googleapis.com/css2?family=Marcellus&family=Rubik:wght@400;500&display=swap">
<style>
:root{
  --blue:#2196d3;
  --blue-dark:#1478b4;
  --green:#8bbd45;
  --green-dark:#6fa233;
  --ink:#333;
  --muted:#555;
  --light:#f3f4f5;
  --white:#fff;
}
*{box-sizing:border-box;margin:0;padding:0}
html,body{width:1200px;height:4549px;overflow:hidden}
body{position:relative;font-family:"Rubik",Arial,sans-serif;color:var(--ink);background:var(--white)}
.abs{position:absolute}
.serif{font-family:"Marcellus",Georgia,serif;font-weight:400}
.btn{position:absolute;display:flex;align-items:center;justify-content:center;gap:8px;border-radius:22px;background:var(--green);color:var(--white);font-size:13px;font-weight:500;letter-spacing:.5px;text-transform:uppercase}
.btn.square{border-radius:0}
.btn.blue{background:var(--blue)}
.eyebrow{position:absolute;font-size:17px;letter-spacing:3px;text-transform:uppercase}
.title{position:absolute;font-family:"Marcellus",Georgia,serif;font-size:36px;letter-spacing:2px;text-transform:uppercase;line-height:1.2}
.rule{position:absolute;height:2px;width:80px;background:var(--blue)}
.copy{position:absolute;font-size:15px;line-height:1.55;color:var(--muted)}
.edge{position:absolute;left:0;width:1200px;height:5px;background:var(--green)}

/* top bar */
.topbar{position:absolute;left:0;top:0;width:1200px;height:28px;background:var(--green)}
.topbar .call{position:absolute;left:718px;top:6px;font-size:12px;color:var(--white);display:flex;align-items:center;gap:6px}
.topbar .book{position:absolute;left:915px;top:0;width:182px;height:28px;background:var(--blue);color:var(--white);font-size:11px;font-weight:500;display:flex;align-items:center;justify-content:center;gap:6px}

/* hero */
.hero-bg{left:0;top:28px;width:1200px;height:692px;background:linear-gradient(180deg,#eef2f5 0%,#dfe8ee 12%,#3d89c0 20%,#1f6fa8 55%,#2d84bd 100%)}
.hero-model{left:620px;top:120px;width:330px;height:598px;background:linear-gradient(180deg,#d8a484 0%,#c98e6c 45%,#f5f5f5 50%,#c98e6c 62%,#d63b36 85%);border-radius:140px 140px 0 0;opacity:.9}
.nav{position:absolute;left:0;top:28px;width:1200px;height:100px;background:rgba(255,255,255,.55)}
.brand{position:absolute;display:flex;align-items:center;gap:10px;color:var(--blue);font-family:"Marcellus",Georgia,serif;font-size:34px}
.brand .dot{width:34px;height:34px;border-radius:50%;background:var(--green)}
.menu{position:absolute;left:422px;top:62px;display:flex;gap:34px;font-size:13px;color:var(--blue);text-transform:uppercase}
.menu .on{border-bottom:2px solid var(--green);padding-bottom:8px}
.contact-pill{position:absolute;left:925px;top:50px;width:148px;height:40px;border:2px solid var(--blue);border-radius:20px;color:var(--blue);font-size:13px;display:flex;align-items:center;justify-content:center}
.hero-ring{left:96px;top:183px;width:450px;height:450px;border-radius:50%;border:2px solid var(--white)}
.hero-circle{left:108px;top:195px;width:426px;height:426px;border-radius:50%;background:var(--blue);color:var(--white);text-align:center}
.hero-circle .sub{position:absolute;left:0;right:0;top:132px;font-size:19px;letter-spacing:1px}
.hero-circle h1{position:absolute;left:0;right:0;top:160px;font-family:"Marcellus",Georgia,serif;font-weight:400;font-size:44px;letter-spacing:4px;line-height:1.15}
.hero-circle .mark{position:absolute;left:188px;top:70px;width:50px;height:50px;border-radius:50%;background:var(--white)}
.arrow{position:absolute;top:345px}

/* about */
.center{left:0;width:1200px;text-align:center}
.card{position:absolute;top:1033px;width:312px;height:228px;border:2px solid var(--blue);border-radius:0 50px 0 50px;text-align:center}
.card.green{border-color:var(--green)}
.card .icon{position:absolute;left:114px;top:-40px;width:84px;height:84px;border-radius:50%;background:var(--blue);display:flex;align-items:center;justify-content:center}
.card.green .icon{background:var(--green)}
.card.teal .icon{background:#2a86a8}
.card .icon span{width:34px;height:34px;border:3px solid var(--white);border-radius:50%}
.card h3{position:absolute;left:0;right:0;top:74px;font-size:16px;font-weight:500;color:var(--blue)}
.card.green h3{color:var(--green-dark)}
.card p{position:absolute;left:30px;right:30px;top:100px;font-size:11.5px;line-height:1.65;color:var(--muted)}

/* program band */
.band-blue{left:0;top:1368px;width:1200px;height:529px;background:linear-gradient(180deg,#2499d6 0%,#2a8fca 60%,#1e74ad 100%)}
.model-yellow{left:53px;top:1306px;width:565px;height:591px;background:linear-gradient(180deg,#e9c49a 0%,#f2d22e 35%,#f5d400 70%,#f0c800 100%);border-radius:260px 260px 0 0}

/* wellness */
.band-light{left:0;top:1900px;width:1200px;height:567px;background:linear-gradient(90deg,#f1f2f3 0%,#eceeef 100%)}
.stones{left:600px;top:1930px;width:600px;height:537px;background:radial-gradient(ellipse at 50% 55%,#e6e2dc 0%,#d4cec5 35%,#eef0f1 70%)}

/* shapes */
.tile{position:absolute;color:var(--white);font-size:16px;font-weight:500;letter-spacing:.5px;text-transform:uppercase;display:flex;align-items:flex-end;padding:0 0 14px 20px}
.tile.couples{left:116px;top:2515px;width:240px;height:221px;background:linear-gradient(160deg,#9fb3c9 0%,#5c7fa4 50%,#2b8fd0 100%)}
.tile.men{left:365px;top:2605px;width:240px;height:219px;background:linear-gradient(160deg,#9aa9b7 0%,#6c7f92 50%,#2b8fd0 100%);border-radius:40px 0 50px 0}
.tile.women{left:120px;top:2748px;width:238px;height:217px;background:linear-gradient(160deg,#c6b7a3 0%,#8a7d5d 50%,#6e9a3c 100%);border-radius:0 0 50px 0}

/* gallery */
.band-green{left:0;top:3027px;width:1200px;height:379px;background:linear-gradient(180deg,#88bd46 0%,#7bb33c 100%)}
.shot{position:absolute}
.label{position:absolute;top:3459px;height:44px;color:var(--white);font-size:18px;font-weight:500;letter-spacing:1px;display:flex;align-items:center;justify-content:center}

/* cta */
.cta-ring{left:632px;top:3566px;width:476px;height:476px;border-radius:50%;border:3px solid var(--green)}
.cta-circle{left:647px;top:3581px;width:446px;height:446px;border-radius:50%;background:linear-gradient(180deg,#2a9ad8 0%,#1f7fbd 100%)}
.athlete{left:600px;top:3560px;width:570px;height:520px;background:radial-gradient(ellipse at 50% 45%,rgba(90,90,96,.75) 0%,rgba(120,110,105,.45) 40%,rgba(0,0,0,0) 65%)}

/* footer */
.footer{left:0;top:4162px;width:1200px;height:295px;background:var(--light)}
.vline{position:absolute;top:4162px;width:1px;height:235px;background:#b9d6ea}
.fhead{position:absolute;top:4234px;font-family:"Marcellus",Georgia,serif;font-size:17px;letter-spacing:1px;color:var(--ink)}
.flist{position:absolute;top:4268px;font-size:12.5px;line-height:26px;color:var(--muted);list-style:none}
.crow{position:absolute;left:890px;display:flex;align-items:flex-start;gap:12px;font-size:12.5px;line-height:16px;color:var(--muted)}
.crow .ic{width:22px;height:22px;border-radius:50%;background:var(--blue);flex:none;display:flex;align-items:center;justify-content:center}
.social{position:absolute;left:198px;top:4320px;display:flex;gap:8px}
.social span{width:28px;height:28px;border-radius:50%;background:var(--green)}
.copyright{left:0;top:4457px;width:1200px;height:92px;border-top:1px solid #dde1e4;text-align:center;font-size:12px;color:#777;line-height:90px}
.copyright u{color:var(--blue)}
</style>
</head>
<body>

<!-- top bar -->
<div class="topbar">
  <div class="call">
    <svg width="14" height="14" viewBox="0 0 24 24"><circle cx="12" cy="12" r="12" fill="#fff"/><path d="M8 6l2 0 1 3-1.5 1a7 7 0 0 0 4 4l1-1.5 3 1v2c0 1-1 2-2 2A10 10 0 0 1 6 8c0-1 1-2 2-2z" fill="#8bbd45"/></svg>
    CALL US <b>(415) 555 0184</b>
  </div>
  <div class="book">BOOK CONSULTATION
    <svg width="16" height="10" viewBox="0 0 16 10"><path d="M0 5h14M10 1l4 4-4 4" stroke="#fff" stroke-width="1.5" fill="none"/></svg>
  </div>
</div>

<!-- hero -->
<div class="abs hero-bg" role="img" aria-label="Calm sea under a pale sky"></div>
<div class="abs hero-model" role="img" aria-label="Athletic woman in a white sports top and red leggings standing by the sea"></div>
<div class="nav"></div>
<div class="brand" style="left:86px;top:52px"><span class="dot"></span>Brightfernrx</div>
<nav class="menu">
  <span class="on">About Us</span><span>Services</span><span>Why Us</span><span>Befor &amp; After</span><span>Blogs</span>
</nav>
<div class="contact-pill">CONTACT US</div>

<svg class="arrow" style="left:26px" width="26" height="46" viewBox="0 0 26 46"><path d="M22 2L4 23l18 21" stroke="#fff" stroke-width="3" fill="none"/></svg>
<svg class="arrow" style="left:1148px" width="26" height="46" viewBox="0 0 26 46"><path d="M4 2l18 21L4 44" stroke="#fff" stroke-width="3" fill="none"/></svg>

<div class="abs hero-ring"></div>
<div class="abs hero-circle">
  <span class="mark"></span>
  <div class="sub">BRIGHTFERNRX</div>
  <h1>WELLNESS AND<br>WEIGHT LOSS</h1>
  <div class="btn" style="left:133px;top:278px;width:172px;height:40px">VIEW SERVICES</div>
</div>
<div class="edge" style="top:718px"></div>

<!-- about -->
<h2 class="abs center serif" style="top:820px;font-size:48px;letter-spacing:3px;color:var(--green-dark)">ABOUT <span style="color:var(--blue)">BRIGHTFERNRX</span></h2>
<div class="rule" style="left:560px;top:885px"></div>
<p class="copy center" style="top:906px;font-size:16px">Lorem ipsum dolor sit amet, consectetur adipiscing elit, sed do eiusmod tempor in-<br>cididunt ut labore et dolore magna aliqua. Ut enim ad minim veniam</p>

<div class="card" style="left:120px">
  <div class="icon"><span></span></div>
  <h3>WEIGHT LOSS</h3>
  <p>Lorem ipsum dolor sit amet, consectetur adipiscing elit, sed do eiusmo.Lorem ipsum dolor sit amet, consectetur adipi-scing elit, sed do eiusmo.</p>
</div>
<div class="card green" style="left:450px;top:1038px">
  <div class="icon"><span></span></div>
  <h3>WELLNESS SERVICE</h3>
  <p>Lorem ipsum dolor sit amet, consectetur adipiscing elit, sed do eiusmo.Lorem ipsum dolor sit amet, consectetur adipi-scing elit, sed do eiusmo.</p>
</div>
<div class="card teal" style="left:779px;top:1040px">
  <div class="icon"><span></span></div>
  <h3>REJUVENATION</h3>
  <p>Lorem ipsum dolor sit amet, consectetur adipiscing elit, sed do eiusmo.Lorem ipsum dolor sit amet, consectetur adipi-scing elit, sed do eiusmo.</p>
</div>

<!-- weight loss program -->
<div class="abs band-blue" role="img" aria-label="Soft blue mountain lake backdrop"></div>
<div class="abs model-yellow" role="img" aria-label="Smiling woman in yellow activewear measuring her waist with a tape"></div>
<div class="eyebrow" style="left:653px;top:1484px;color:#fff">Medically Supervised</div>
<div class="title" style="left:653px;top:1510px;color:#fff;font-size:32px">Weight Loss Program</div>
<div class="rule" style="left:655px;top:1556px;background:#fff"></div>
<p class="copy" style="left:658px;top:1576px;width:400px;color:#fff;font-size:15.5px">Lorem ipsum dolor sit amet, consectetur adipi-scing elit, sed do eiusmod tempor incididunt ut labore et dolore magna aliqua. Ut enim ad minim veniam, quis nostrud exercitation ullamco laboris nisi ut aliquip ex ea commodo consequat.</p>
<div class="btn" style="left:658px;top:1713px;width:172px;height:40px">LEARN MORE</div>
<div class="edge" style="top:1895px;height:4px"></div>

<!-- wellness service -->
<div class="abs band-light"></div>
<div class="abs stones" role="img" aria-label="Stacked white pebbles reflected in still water"></div>
<div class="eyebrow" style="left:116px;top:2058px;color:var(--ink)">Care &amp; Wellness</div>
<div class="title" style="left:116px;top:2084px;color:var(--green-dark);font-size:38px">Wellness Service</div>
<div class="rule" style="left:118px;top:2136px"></div>
<p class="copy" style="left:120px;top:2156px;width:390px">Lorem ipsum dolor sit amet, consectetur adipiscing elit, sed do eiusmod tempor incididunt ut labore et dolore magna aliqua. Ut enim ad minim veniam, quis nostrud exercitation ullamco laboris nisi</p>
<div class="btn" style="left:114px;top:2274px;width:172px;height:40px">LEARN MORE</div>

<!-- shapes & sizes -->
<div class="tile couples" role="img" aria-label="Smiling couple in casual clothes">For Couples</div>
<div class="tile men" role="img" aria-label="Man sitting on a bed by a window">For Mens</div>
<div class="tile women" role="img" aria-label="Woman sitting on the floor at home">For Women</div>
<div class="eyebrow" style="left:648px;top:2580px;color:var(--ink);font-size:16px">Weight Loss</div>
<div class="title" style="left:648px;top:2608px;color:var(--blue);font-size:34px;line-height:1.3">We Help All<br>Shapes &amp; Sizes</div>
<div class="rule" style="left:650px;top:2704px;background:var(--green)"></div>
<p class="copy" style="left:652px;top:2724px;width:410px">Lorem ipsum dolor sit amet, consectetur adipiscing elit, sed do eiusmod tempor incididunt ut labore et dolore magna aliqua. Ut enim ad minim veniam, quis nostrud exercitation ullamco laboris nisi</p>
<div class="btn" style="left:650px;top:2852px;width:184px;height:44px">LEARN MORE</div>

<!-- gallery -->
<div class="abs band-green" role="img" aria-label="Soft green hills backdrop"></div>
<div class="eyebrow center" style="top:3086px;color:#fff;font-size:14px">Before &amp; After Gallery</div>
<div class="title center" style="top:3110px;color:#fff;font-size:38px">Real Success Stories</div>
<div class="rule" style="left:560px;top:3164px;background:#fff"></div>

<div class="shot" style="left:124px;top:3260px;width:150px;height:199px;background:linear-gradient(180deg,#e8e6e4 0%,#d5b39a 35%,#cfe64a 55%,#8e2f33 80%)" role="img" aria-label="Woman before weight loss, front view"></div>
<div class="shot" style="left:278px;top:3260px;width:146px;height:199px;background:linear-gradient(180deg,#e8e6e4 0%,#d5b39a 35%,#cfe64a 55%,#8e2f33 80%)" role="img" aria-label="Woman before weight loss, side view"></div>
<div class="shot" style="left:424px;top:3230px;width:184px;height:229px;background:linear-gradient(180deg,#f0efee 0%,#d8b59c 35%,#2a2a2a 50%,#d8b59c 65%,#1e1e1e 85%,#e2e0de 100%)" role="img" aria-label="Woman before weight loss in black swimwear"></div>
<div class="shot" style="left:608px;top:3230px;width:184px;height:229px;background:linear-gradient(180deg,#f0efee 0%,#d8b59c 35%,#2a2a2a 50%,#d8b59c 65%,#1e1e1e 85%,#e2e0de 100%)" role="img" aria-label="Woman after weight loss in black swimwear"></div>
<div class="shot" style="left:792px;top:3260px;width:146px;height:199px;background:linear-gradient(180deg,#eceae8 0%,#6b4a36 40%,#5a3c2b 65%,#4d6f99 85%)" role="img" aria-label="Man before weight loss"></div>
<div class="shot" style="left:942px;top:3260px;width:147px;height:199px;background:linear-gradient(180deg,#eceae8 0%,#6b4a36 40%,#5a3c2b 65%,#4d6f99 85%)" role="img" aria-label="Man after weight loss"></div>
<div class="label" style="left:424px;width:184px;background:var(--blue)">BEFORE</div>
<div class="label" style="left:608px;width:184px;background:var(--green)">AFTER</div>

<!-- call to action -->
<div class="eyebrow" style="left:132px;top:3630px;color:var(--blue);font-size:19px">Get Start Today!</div>
<div class="title" style="left:132px;top:3662px;color:var(--ink);font-size:38px;line-height:1.17">Call Us Today or<br>Schedule Your<br>Appointment!</div>
<p class="copy" style="left:132px;top:3822px;width:440px">Lorem ipsum dolor sit amet, consectetur adipiscing elit, sed do eiusmod tempor incididunt ut labore et dolore magna aliqua. Ut enim ad minim veniam</p>
<div class="btn square" style="left:132px;top:3925px;width:191px;height:46px;font-size:15px;text-transform:none">
  <svg width="16" height="16" viewBox="0 0 16 16"><rect x="1" y="3" width="14" height="12" rx="1" fill="none" stroke="#fff" stroke-width="1.5"/><path d="M1 7h14M5 1v4M11 1v4" stroke="#fff" stroke-width="1.5"/></svg>
  BOOK NOW
</div>
<div class="btn square blue" style="left:335px;top:3925px;width:189px;height:46px;font-size:15px">
  <svg width="16" height="16" viewBox="0 0 24 24"><path d="M6 2l4 1 1 5-2.5 1.5a12 12 0 0 0 6 6L16 13l5 1 1 4c0 2-2 4-4 4A18 18 0 0 1 2 6c0-2 2-4 4-4z" fill="#fff"/></svg>
  (415) 555 0184
</div>
<div class="abs cta-ring"></div>
<div class="abs cta-circle"></div>
<div class="abs athlete" role="img" aria-label="Athletic woman doing a push-up in front of a blue circle"></div>

<!-- footer -->
<div class="abs footer"></div>
<div class="brand" style="left:120px;top:4240px;font-size:32px"><span class="dot" style="width:30px;height:30px"></span>Brightfernrx</div>
<div class="social"><span></span><span></span><span></span><span></span></div>

<div class="vline" style="left:445px"></div>
<div class="vline" style="left:625px"></div>
<div class="vline" style="left:868px"></div>

<div class="fhead" style="left:466px">COMPANY</div>
<ul class="flist" style="left:470px"><li>About Us</li><li>Services</li><li>Why Us</li><li>Contact Us</li></ul>

<div class="fhead" style="left:647px">HOURS</div>
<ul class="flist" style="left:651px"><li>Working Hours</li><li>Mon, Tue, Thur, &amp; Fri 9am–6pm</li><li>Sat 9am–4pm</li></ul>

<div class="fhead" style="left:886px">CONTACT US</div>
<div class="crow" style="top:4270px">
  <span class="ic"><svg width="10" height="12" viewBox="0 0 10 12"><path d="M5 12S0 6.5 0 4.5a5 5 0 0 1 10 0C10 6.5 5 12 5 12z" fill="#fff"/><circle cx="5" cy="4.5" r="1.8" fill="#2196d3"/></svg></span>
  <span>2140 Harlow Ridge Rd Ste 210<br>Cedar Falls, Iowa 50613</span>
</div>
<div class="crow" style="top:4316px">
  <span class="ic"><svg width="11" height="11" viewBox="0 0 24 24"><path d="M6 2l4 1 1 5-2.5 1.5a12 12 0 0 0 6 6L16 13l5 1 1 4c0 2-2 4-4 4A18 18 0 0 1 2 6c0-2 2-4 4-4z" fill="#fff"/></svg></span>
  <span style="line-height:22px">319-555-0142</span>
</div>
<div class="crow" style="top:4350px">
  <span class="ic"><svg width="12" height="9" viewBox="0 0 12 9"><rect x=".5" y=".5" width="11" height="8" fill="none" stroke="#fff"/><path d="M.5 .5L6 5l5.5-4.5" fill="none" stroke="#fff"/></svg></span>
  <span style="line-height:22px">info@brightfernrx.com</span>
</div>

<div class="abs copyright">Copyright © 2023 <u>BRIGHTFERNRX</u>. All Right Reserved</div>

</body>
</html>
```